Business Card Design Project

for a second hand vintage clothing store. shop name is The Velvet Cupboard

Cards to be double sided

The name on the card is Joanna Whitfield

Information to put on card:

The Velvet Cupboard
Joanna Whitfield (no job title)
42/871 Dunmore St, Glenwick, Sydney, NSW, 2009.
Mobile: 0412 905 261
Email: thevelvetcupboard@mailbox.com.au
Web: www.thevelvetcupboard.com.au

Target Market(s)

Women looking at vintage clothing

Industry/Entity Type

Clothing

```html
<!DOCTYPE html>
<html lang="en">
<head>
<meta charset="utf-8">
<title>The Velvet Cupboard – Business Card</title>
<link rel="stylesheet" href="https://fonts.googleapis.com/css2?family=Arimo:wght@400;700&display=swap">
<style>
  :root {
    --maroon: #552233;
    --cream: #ead591;
    --tan: #d4b57a;
    --backdrop: #e6e3dd;
    --text-font: "Arimo", Arial, sans-serif;
  }
  * { box-sizing: border-box; margin: 0; padding: 0; }
  html, body { width: 1200px; height: 875px; overflow: hidden; }
  body { background: var(--backdrop); font-family: var(--text-font); position: relative; }

  .card { position: absolute; overflow: hidden; box-shadow: 0 6px 18px rgba(0,0,0,.25); }

  /* Front: portrait card */
  .card-front {
    left: 110px; top: 172px; width: 326px; height: 531px;
    background: var(--cream);
  }
  .card-front .dress-art {
    position: absolute; left: 92px; top: 66px; width: 150px; height: 330px;
    background: linear-gradient(180deg, rgba(212,181,122,.55), var(--tan) 55%, rgba(212,181,122,.7));
    border-radius: 45% 55% 30% 40% / 20% 25% 15% 20%;
  }
  .card-front .wordmark {
    position: absolute; left: 0; right: 0; top: 424px;
    text-align: center; color: var(--maroon);
    font-weight: 400; font-size: 26px; letter-spacing: .3px;
  }
  .card-front .web-band {
    position: absolute; left: 0; right: 0; bottom: 0; height: 34px;
    background: var(--maroon);
    border-radius: 34px 34px 0 0 / 14px 14px 0 0;
    color: var(--cream); font-size: 13px; letter-spacing: .3px;
    display: flex; align-items: center; justify-content: center;
  }

  /* Back: landscape card */
  .card-back {
    left: 540px; top: 272px; width: 531px; height: 326px;
    background: var(--maroon);
  }
  .card-back .wordmark {
    position: absolute; left: 60px; top: 118px;
    display: flex; align-items: center; gap: 12px;
    color: var(--cream); font-weight: 400; font-size: 40px; letter-spacing: .5px;
  }
  .card-back .wordmark .mark-dot {
    width: 14px; height: 14px; border-radius: 50%; background: var(--cream);
  }
  .card-back .info-band {
    position: absolute; left: 0; right: 0; bottom: 0; height: 106px;
    background: var(--cream);
    border-radius: 0 60px 0 0 / 0 26px 0 0;
    color: var(--maroon); font-size: 13px; line-height: 1.35; letter-spacing: .3px;
  }
  .card-back .contact { position: absolute; left: 24px; bottom: 16px; }
  .card-back .contact .name { font-weight: 700; font-size: 15px; margin-bottom: 3px; }
  .card-back .address { position: absolute; right: 24px; top: 20px; }
</style>
</head>
<body>
  <section class="card card-front" aria-label="Business card front">
    <div class="dress-art" role="img" aria-label="Soft painted vintage dress silhouette"></div>
    <div class="wordmark">The Velvet Cupboard</div>
    <div class="web-band">www.thevelvetcupboard.com.au</div>
  </section>

  <section class="card card-back" aria-label="Business card back">
    <div class="wordmark"><span>The Velvet Cupboard</span><span class="mark-dot"></span></div>
    <div class="info-band">
      <div class="address">42/871 Dunmore St, Glenwick,<br>Sydney, NSW, 2009.</div>
      <div class="contact">
        <p class="name">Joanna Whitfield</p>
        <p>M: 0412 905 261</p>
        <p>E: thevelvetcupboard@mailbox.com.au</p>
      </div>
    </div>
  </section>
</body>
</html>
```